依頼詳細
銀座4丁目に高級時計とソルヴェーヌを扱う店舗になります。
入口入ってすぐにLEDで光る看板あるのでそちらのデザインお願いしたいと思います。
派手なものは貸主が駄目と言っていますので、高級感のあるシックな感じでお願いしたいです。
ロゴは数種類のパターンで添付しますので、それを利用してください。
あとはBuy&Sellという文章も挿入してください。
ちなみにLED看板のサイズは縦180cm横120cmのはめ込み式です。
店舗の外観も写真添付しますので参考にしてください。(前に入居してたテナントの写真です)
アーチ状の入口、窓です。
宜しくお願い致します。
記載項目
朔星トレーディング株式会社
店舗名:Velmo(ヴェルモ)
希望イメージ
シンプル 複雑
単色 カラフル
暗い 明るい
日常 高級
遊び心 厳粛
未来的 伝統的
女性的 男性的
希望する色
青系、無彩色系
納品ファイル
• 高解像度JPG (.jpg)
• PNG形式 (.png)
補足説明
会社名は不要です。
文字は店名とBuy&Sellを挿入してください。
■ 選んだ理由

一目で時計屋とわかるデザイン。
シックで高級感あり。

■ 提案者全員のお礼・コメント

最後の修正も迅速に対応して頂きありがとうございました。

```html
<!DOCTYPE html>
<html lang="ja">
<head>
<meta charset="utf-8">
<title>Velmo — Buy &amp; Sell サイン</title>
<link rel="stylesheet" href="https://fonts.googleapis.com/css2?family=Cinzel:wght@600&family=Pinyon+Script&display=swap">
<style>
  :root {
    --page: #ffffff;
    --panel-dark: #2a2d2c;
    --panel-mid: #3d4140;
    --panel-light: #4b504e;
    --facet-deep: #222524;
    --edge-glow: #f4efe2;
    --gold: #d9c08a;
    --logo-white: #f5f5f2;
  }
  * { margin: 0; padding: 0; box-sizing: border-box; }
  html, body {
    width: 896px;
    height: 1200px;
    overflow: hidden;
    background: var(--page);
  }
  .sign {
    position: absolute;
    left: 148px;
    top: 150px;
    width: 600px;
    height: 900px;
    overflow: hidden;
    background: var(--panel-dark);
  }
  .sign-facets {
    position: absolute;
    inset: 0;
    width: 100%;
    height: 100%;
  }
  .store-name {
    position: absolute;
    left: 0;
    right: 0;
    top: 332px;
    display: flex;
    align-items: center;
    justify-content: center;
    gap: 14px;
    font-family: "Cinzel", serif;
    font-weight: 600;
    font-size: 56px;
    letter-spacing: 4px;
    color: var(--logo-white);
  }
  .store-name .mark {
    width: 14px;
    height: 14px;
    border-radius: 50%;
    background: var(--logo-white);
  }
  .tagline {
    position: absolute;
    left: 0;
    right: 0;
    top: 455px;
    text-align: center;
    font-family: "Pinyon Script", cursive;
    font-size: 92px;
    line-height: 1;
    color: var(--gold);
  }
</style>
</head>
<body>
  <main class="sign">
    <svg class="sign-facets" viewBox="0 0 600 900" aria-hidden="true">
      <defs>
        <radialGradient id="diamond-core" cx="50%" cy="45%" r="60%">
          <stop offset="0" stop-color="#3a3e3d"/>
          <stop offset="1" stop-color="#1f2221"/>
        </radialGradient>
        <linearGradient id="glow-line" x1="0" y1="0" x2="1" y2="0">
          <stop offset="0" stop-color="#f4efe2" stop-opacity="0"/>
          <stop offset="0.5" stop-color="#f4efe2" stop-opacity="1"/>
          <stop offset="1" stop-color="#f4efe2" stop-opacity="0"/>
        </linearGradient>
      </defs>
      <!-- outer facets -->
      <polygon points="0,0 600,0 300,225" fill="var(--panel-mid)"/>
      <polygon points="0,0 300,225 15,470 0,470" fill="var(--panel-light)"/>
      <polygon points="600,0 600,470 585,470 300,225" fill="var(--panel-dark)"/>
      <polygon points="0,470 15,470 300,720 0,900" fill="var(--panel-dark)"/>
      <polygon points="600,470 585,470 300,720 600,900" fill="var(--panel-mid)"/>
      <polygon points="0,900 300,720 600,900" fill="var(--panel-light)"/>
      <polygon points="0,640 180,620 0,780" fill="var(--facet-deep)" opacity="0.6"/>
      <polygon points="600,120 440,150 600,300" fill="var(--panel-light)" opacity="0.5"/>
      <!-- central diamond -->
      <polygon points="300,225 585,470 300,720 15,470" fill="url(#diamond-core)"/>
      <polygon points="300,225 585,470 300,720 15,470" fill="none" stroke="var(--edge-glow)" stroke-opacity="0.35" stroke-width="1.5"/>
      <!-- glowing diagonals -->
      <line x1="120" y1="110" x2="300" y2="225" stroke="url(#glow-line)" stroke-width="2"/>
      <line x1="430" y1="340" x2="585" y2="470" stroke="url(#glow-line)" stroke-width="2"/>
      <line x1="15" y1="470" x2="170" y2="605" stroke="url(#glow-line)" stroke-width="2"/>
      <line x1="330" y1="700" x2="520" y2="830" stroke="url(#glow-line)" stroke-width="2"/>
      <line x1="470" y1="0" x2="600" y2="80" stroke="url(#glow-line)" stroke-width="1.5"/>
    </svg>
    <div class="store-name"><span class="mark"></span>VELMO</div>
    <p class="tagline">Buy &amp; Sell</p>
  </main>
</body>
</html>
```